Veteran Owned General Contractor needs Bold New Business Cards

We are a service disabled veteran owned small business. We're a general contractor that specializes in excavation, underground utilities, site work, land clearing and demolition. We would like a fresh, simple, bold, new look for our business cards. We're open to ideas! We'd like to incorporate the following information on the card:

Company Name & Logo, Name of Person, Job Title, Office Phone, Fax, Cell Phone, Email Address, Website, SDVOSB

Our logo is included. We look forward to your thoughts.

Thank you!
Updates

Reason: Hello Due to the overwhelming response to this project, we are extending the deadline one time to allow for improved communication and feedback with the top candidates. We would like to thank everyone for their hard work and exceptional creativity! Thank you

Industry/Entity Type

Business

Contact Information for Business Card

Font styles to use
Sans Serif

Requirements
Nice to have
• As we are a veteran owned company, it would be nice to incorporate an American flag into the design. Maybe on the back?

```html
<!DOCTYPE html>
<html lang="en">
<head>
<meta charset="utf-8">
<title>Brackwell Inc – Business Card</title>
<link rel="stylesheet" href="https://fonts.googleapis.com/css2?family=Montserrat:wght@600;800&display=swap">
<style>
  :root {
    --bg-top: #1c1b20;
    --bg-bottom: #36343f;
    --card: #ffffff;
    --green: #5abd2c;
    --ink: #111111;
  }
  * { box-sizing: border-box; margin: 0; padding: 0; }
  html, body { width: 1200px; height: 1173px; overflow: hidden; }
  body {
    background: linear-gradient(180deg, var(--bg-top), var(--bg-bottom));
    font-family: "Montserrat", sans-serif;
    position: relative;
  }
  .card {
    position: absolute;
    left: 250px;
    width: 700px;
    height: 400px;
    background: var(--card);
    border-radius: 26px;
    overflow: hidden;
    box-shadow: 0 24px 50px rgba(0,0,0,.45);
  }
  .card--front { top: 120px; }
  .card--back { top: 640px; }

  .brand { display: flex; align-items: center; gap: 16px; }
  .brand__square { width: 56px; height: 56px; background: var(--ink); border-radius: 6px; flex: none; }
  .brand__name {
    font-weight: 800;
    color: var(--green);
    letter-spacing: 1px;
    line-height: 1;
    white-space: nowrap;
  }

  .card--front .brand { position: absolute; left: 44px; top: 46px; }
  .card--front .brand__name { font-size: 50px; }

  .divider {
    position: absolute;
    left: 372px; top: 150px;
    width: 2px; height: 150px;
    background: var(--green);
  }

  .person { position: absolute; left: 60px; top: 262px; }
  .person__name { font-size: 34px; font-weight: 800; color: var(--ink); line-height: 1.1; }
  .person__title { font-size: 18px; font-weight: 600; color: var(--ink); margin-left: 26px; }

  .contacts {
    position: absolute;
    right: 40px; top: 140px;
    list-style: none;
    display: flex; flex-direction: column; gap: 14px;
    align-items: flex-end;
  }
  .contact { display: flex; align-items: center; gap: 10px; font-size: 17px; font-weight: 600; color: var(--ink); }
  .contact__icon {
    width: 34px; height: 34px; border-radius: 50%;
    background: var(--green);
    display: flex; align-items: center; justify-content: center;
  }
  .contact__icon svg { width: 18px; height: 18px; }

  .band { position: absolute; left: 0; bottom: 0; width: 100%; height: 20px; background: var(--green); }

  .card--back .brand {
    position: absolute; inset: 0;
    flex-direction: column; justify-content: center; gap: 24px;
  }
  .card--back .brand__square { width: 110px; height: 110px; border-radius: 12px; }
  .card--back .brand__name { font-size: 58px; }
</style>
</head>
<body>
  <section class="card card--front">
    <div class="brand">
      <div class="brand__square"></div>
      <span class="brand__name">BRACKWELL INC</span>
    </div>

    <div class="divider"></div>

    <div class="person">
      <div class="person__name">Name</div>
      <div class="person__title">Job Title</div>
    </div>

    <ul class="contacts">
      <li class="contact">Phone
        <span class="contact__icon"><svg viewBox="0 0 24 24" fill="#fff"><path d="M6.6 10.8a15 15 0 0 0 6.6 6.6l2.2-2.2c.3-.3.7-.4 1-.2 1.1.4 2.3.6 3.6.6.6 0 1 .4 1 1V20c0 .6-.4 1-1 1A17 17 0 0 1 3 4c0-.6.4-1 1-1h3.5c.6 0 1 .4 1 1 0 1.3.2 2.5.6 3.6.1.3 0 .7-.2 1z"/></svg></span>
      </li>
      <li class="contact">Email
        <span class="contact__icon"><svg viewBox="0 0 24 24" fill="none" stroke="#fff" stroke-width="2"><rect x="3" y="6" width="18" height="12" rx="1"/><path d="M3 6l9 7 9-7"/></svg></span>
      </li>
      <li class="contact">Website
        <span class="contact__icon"><svg viewBox="0 0 24 24" fill="none" stroke="#fff" stroke-width="2"><circle cx="12" cy="12" r="9"/><path d="M3 12h18M12 3c3 3 3 15 0 18M12 3c-3 3-3 15 0 18"/></svg></span>
      </li>
      <li class="contact">Address
        <span class="contact__icon"><svg viewBox="0 0 24 24" fill="#fff"><path d="M12 3l9 8h-3v9h-4v-6h-4v6H6v-9H3z"/></svg></span>
      </li>
    </ul>

    <div class="band"></div>
  </section>

  <section class="card card--back">
    <div class="brand">
      <div class="brand__square"></div>
      <span class="brand__name">BRACKWELL INC</span>
    </div>
  </section>
</body>
</html>
```